Business card for Financial Technology company

Hello! We'd like to create business cards for 4 members of our company. Our company is a financial technology business that provides funding for businesses. We want to give it a VC (venture captal) look and feel. Clean, fresh and minimal but with a flair of artistry. I'll include some samples of cards we like. It would be great if the back of the card was artistic (see sample files 1 and 2) and the front of the card was the business info. The name of the company is Q7 Funding.

```html
<!DOCTYPE html>
<html lang="en">
<head>
<meta charset="utf-8">
<title>Q7 Funding — Business Card</title>
<link rel="stylesheet" href="https://fonts.googleapis.com/css2?family=Montserrat:wght@400;700;800&display=swap">
<style>
  :root {
    --stage: #e9e6e1;
    --card: #0b0b0c;
    --ink: #ffffff;
    --ink-soft: #e6e6e6;
    --violet: #4b3a8f;
    --magenta: #d62a8a;
    --orange: #f08a2c;
    --teal: #1f8fa6;
    --green: #4bb34a;
  }
  * { box-sizing: border-box; margin: 0; padding: 0; }
  html, body { width: 1200px; height: 864px; overflow: hidden; }
  body {
    background: var(--stage);
    font-family: "Montserrat", Arial, sans-serif;
    display: flex;
    align-items: center;
    justify-content: center;
    gap: 60px;
  }
  .card {
    width: 420px;
    height: 720px;
    background: var(--card);
    color: var(--ink);
    position: relative;
    overflow: hidden;
    border-radius: 4px;
    box-shadow: 0 10px 30px rgba(0,0,0,0.25);
  }

  /* Back of card */
  .card-back .artwork {
    position: absolute;
    inset: 0 0 auto 0;
    height: 440px;
    background:
      radial-gradient(circle at 20% 20%, var(--orange) 0 8%, transparent 30%),
      radial-gradient(circle at 70% 15%, var(--teal) 0 10%, transparent 35%),
      radial-gradient(circle at 85% 55%, var(--magenta) 0 6%, transparent 30%),
      radial-gradient(circle at 40% 45%, var(--green) 0 5%, transparent 28%),
      linear-gradient(160deg, var(--violet), #2a2250 60%, transparent);
    -webkit-mask-image: linear-gradient(200deg, #000 40%, transparent 85%);
            mask-image: linear-gradient(200deg, #000 40%, transparent 85%);
  }
  .card-back .company-name {
    position: absolute;
    left: 0; right: 0;
    top: 520px;
    text-align: center;
    font-weight: 700;
    font-size: 40px;
    line-height: 1;
  }

  /* Front of card */
  .card-front .company-line {
    position: absolute;
    top: 120px;
    left: 0; right: 0;
    display: flex;
    align-items: center;
    justify-content: center;
    gap: 14px;
    font-weight: 700;
    font-size: 40px;
    line-height: 1;
  }
  .company-line .square {
    width: 20px;
    height: 20px;
    background: var(--magenta);
  }
  .card-front .details {
    position: absolute;
    top: 330px;
    left: 0; right: 0;
    text-align: center;
  }
  .person-name {
    font-weight: 800;
    font-size: 36px;
    letter-spacing: 1px;
    line-height: 1.1;
  }
  .person-title {
    font-weight: 400;
    font-size: 18px;
    margin-top: 6px;
    color: var(--ink-soft);
  }
  .rule {
    width: 230px;
    height: 2px;
    background: var(--ink);
    margin: 12px auto 26px;
  }
  .contact {
    list-style: none;
    font-size: 17px;
    line-height: 1.65;
    color: var(--ink-soft);
  }
</style>
</head>
<body>
  <section class="card card-back" aria-label="Card back">
    <div class="artwork" role="img" aria-label="Colourful hand-drawn swirl illustration in violet, teal, orange, magenta and green"></div>
    <p class="company-name">Q7 Funding</p>
  </section>

  <section class="card card-front" aria-label="Card front">
    <p class="company-line"><span class="square"></span>Q7 Funding</p>
    <div class="details">
      <h1 class="person-name">YOUR NAME</h1>
      <p class="person-title">Your Tittle Here</p>
      <div class="rule"></div>
      <ul class="contact">
        <li>012 345 6789 | Fax 012 345 6789</li>
        <li>Your@q7mail.com</li>
        <li>www.Yourwebsite.com</li>
        <li>No.000, Your Street, Province,</li>
        <li>Your Country</li>
      </ul>
    </div>
  </section>
</body>
</html>
```